Initial website for sport tech startup

We are currently in the R&D phases of our new product. It’s a headband to prevent concussion in the soccer market initially.

We have 2 products, one that’s basic aimed at the youth market and the other more technology driven that’s aimed at the academies and professional market.

Initially the product will launch in the UK

Target Market(s)

Youth soccer players and parents in UK, Soccer Clubs, Federations.

Industry/Entity Type

Sporting Good

Coding

Coded - Design and coding required

Number of Pages Required

5+ page

Requirements
Must have
• Professional style that can be adapted and changed over the coming months.
Nice to have
• Ecommerce ability in the future.

```html
<!DOCTYPE html>
<html lang="en">
<head>
<meta charset="utf-8">
<title>Halomark – Head Protection for Football</title>
<link href="https://fonts.googleapis.com/css2?family=Lato:wght@400;700;900&display=swap" rel="stylesheet">
<style>
:root{
  --blue:#0c4b88;
  --blue-dark:#0a3f75;
  --ink:#3a3a3a;
  --text:#555;
  --btn:#565656;
  --icon:#58595b;
  --grey:#f3f3f3;
  --footer:#262626;
  --line:#666;
  --white:#fff;
}
*{margin:0;padding:0;box-sizing:border-box}
html,body{width:1200px;height:4894px;overflow:hidden}
body{position:relative;font-family:"Lato",sans-serif;color:var(--text);background:var(--white)}
.abs{position:absolute}
a{color:inherit;text-decoration:none}

/* header */
.topbar{top:14px;right:72px;display:flex;gap:24px;font-size:15px;color:var(--blue);font-weight:700}
.topbar span{display:flex;align-items:center;gap:8px}
.brand{left:76px;top:42px;width:240px;height:57px;border:3px solid var(--blue);display:flex;align-items:center;justify-content:center;font-size:38px;font-weight:700;color:var(--blue);letter-spacing:1px}
.nav{top:80px;right:72px;display:flex;gap:8px;font-size:13px;color:var(--ink)}
.nav a{padding:8px 16px;border:2px solid transparent}
.nav a.active{border-color:var(--blue);color:var(--blue)}

/* hero */
.hero{top:142px;left:0;width:1200px;height:735px;background:linear-gradient(160deg,#6a7a45 0%,#3f5a2b 35%,#c9cfd6 55%,#4d6a33 75%,#2f4422 100%)}
.hero-text{top:320px;left:0;width:1200px;text-align:center;color:var(--white);text-shadow:0 2px 6px rgba(0,0,0,.45)}
.hero-text .kicker{font-size:48px;font-weight:700;line-height:1}
.hero-text h1{font-size:92px;font-weight:900;line-height:1;margin-top:4px}
.hero-text p{font-size:29px;margin-top:28px}
.dots{top:674px;left:565px;display:flex;gap:10px}
.dots i{width:10px;height:10px;border-radius:50%;background:var(--white)}
.dots i:first-child{background:#4ab3e8}

/* bracket frame: open on the right, short returns at top and bottom */
.bracket{border:2px solid var(--line);border-right:none;z-index:3}
.bracket::before,.bracket::after{content:"";position:absolute;right:0;width:2px;background:var(--line)}
.bracket::before{top:0;height:16px}
.bracket::after{bottom:0;height:32px}

/* text block beside the bracket */
.copy-block{z-index:4}
.copy-block .eyebrow{font-size:27px;color:var(--ink);font-weight:400;line-height:1.2}
.copy-block h2{font-size:33px;color:var(--blue);font-weight:700;line-height:1.15;margin-bottom:14px}
.copy-block p{font-size:13.5px;line-height:26px;color:#555}
.btn{display:inline-block;background:var(--btn);color:var(--white);font-size:13px;font-weight:700;padding:11px 32px;margin-top:24px}
.photo{z-index:3}

/* mission */
.mission{top:1410px;left:0;width:1200px;text-align:center;color:var(--white);z-index:2}
.mission h2{font-size:32px;font-weight:700}
.mission h3{font-size:21px;font-weight:700;margin-top:18px}
.mission p{width:920px;margin:22px auto 0;font-size:13.5px;line-height:26px}

/* features */
.rule{top:2161px;left:76px;width:1050px;height:1px;background:#bbb}
.section-title{left:0;width:1200px;text-align:center;font-size:33px;font-weight:700;color:var(--blue)}
.feature{width:260px;text-align:center}
.feature .circle{width:108px;height:108px;border-radius:50%;background:var(--icon);margin:0 auto;display:flex;align-items:center;justify-content:center}
.feature .label{font-size:13px;font-weight:700;color:var(--blue);margin-top:30px}

/* team */
.team-title{color:var(--ink);font-weight:400}
.member{width:300px;text-align:center}
.member .portrait{width:98px;height:98px;margin:0 auto;background:linear-gradient(160deg,#d8c8b8,#8a7a6e)}
.member h4{font-size:14px;color:var(--blue);font-weight:700;margin-top:28px}
.member .role{font-size:11.5px;color:var(--ink);font-weight:700;margin-top:6px}
.member p{font-size:13px;line-height:26px;margin-top:8px}

/* distribution */
.dist p{width:960px;margin:20px auto 0;font-size:13.5px;line-height:26px;text-align:center}
.partners{top:4354px;left:0;width:1200px;display:flex;justify-content:center;gap:60px;align-items:center}
.partners i{display:block;background:#333;border-radius:8px}

/* newsletter */
.newsletter{top:4499px;left:0;width:1200px;height:106px;background:var(--blue-dark);color:var(--white)}
.newsletter .label{position:absolute;left:76px;top:40px;font-size:21px}
.newsletter .field{position:absolute;left:330px;top:30px;width:325px;height:46px;background:var(--white);color:#333;font-size:15px;padding:14px 18px}
.newsletter .go{position:absolute;left:652px;top:28px;width:50px;height:50px;border-radius:50%;background:#222;color:var(--white);font-weight:900;font-size:19px;display:flex;align-items:center;justify-content:center}
.newsletter .follow{position:absolute;left:920px;top:26px;font-size:17px}
.newsletter .socials{position:absolute;left:918px;top:56px;display:flex;gap:22px}
.newsletter .socials i{width:24px;height:24px;border-radius:50%;background:var(--white)}

/* footer */
.footer{top:4605px;left:0;width:1200px;height:289px;background:var(--footer);color:#ccc}
.footer .f-brand{position:absolute;left:76px;top:104px;width:216px;height:50px;border:3px solid var(--white);color:var(--white);font-size:34px;font-weight:700;display:flex;align-items:center;justify-content:center}
.footer .copy{position:absolute;left:76px;top:168px;font-size:13px;line-height:24px}
.footer .col{position:absolute;top:46px}
.footer h5{font-size:16px;color:var(--white);font-weight:700;margin-bottom:14px}
.footer ul{list-style:none;font-size:13px;line-height:33px}
.footer .split{display:flex;gap:60px}
</style>
</head>
<body>

<!-- header -->
<div class="abs topbar">
  <span><svg width="14" height="14" viewBox="0 0 24 24"><path fill="#0c4b88" d="M6.6 10.8a15 15 0 006.6 6.6l2.2-2.2a1 1 0 011-.25 11.4 11.4 0 003.6.57 1 1 0 011 1V20a1 1 0 01-1 1A17 17 0 013 4a1 1 0 011-1h3.5a1 1 0 011 1c0 1.25.2 2.45.57 3.570a1 1 0 01-.25 1z"/></svg>+44 20 7946 0321</span>
  <span><svg width="15" height="12" viewBox="0 0 24 18"><rect width="24" height="18" rx="2" fill="#0c4b88"/><path d="M1 1l11 9 11-9" stroke="#fff" stroke-width="2" fill="none"/></svg>hello@halomark.example</span>
</div>
<div class="abs brand">HALOMARK</div>
<nav class="abs nav">
  <a class="active" href="#">HOME</a><a href="#">ABOUT US</a><a href="#">SERVICES</a><a href="#">PRODUCTS</a><a href="#">CLIENTS</a><a href="#">NEWS</a><a href="#">CONTACT US</a>
</nav>

<!-- hero -->
<div class="abs hero" role="img" aria-label="Photo of footballers on the pitch attending to an injured player"></div>
<svg class="abs" style="top:640px;left:0" width="1200" height="240" viewBox="0 0 1200 240">
  <path fill="#fff" d="M0 150 C150 150 280 240 430 230 C580 220 640 120 780 80 C920 40 1050 140 1200 130 L1200 240 L0 240Z"/>
</svg>
<div class="abs hero-text">
  <div class="kicker">WELCOME TO</div>
  <h1>HALOMARK</h1>
  <p>Vestibulum ante ipsum primis in faucibus orci luctus et ultrices</p>
</div>
<div class="abs dots"><i></i><i></i><i></i><i></i></div>

<!-- mission band -->
<svg class="abs" style="top:1240px;left:0;z-index:1" width="1200" height="560" viewBox="0 0 1200 560">
  <path fill="#0c4b88" d="M0 24 C120 14 220 90 400 84 C560 78 620 30 700 20 C900 0 1000 -10 1200 10 L1200 450 C1100 420 1000 500 900 480 C800 460 760 400 650 420 C500 450 350 540 0 540 Z"/>
</svg>

<div class="abs bracket" style="left:74px;top:935px;width:424px;height:373px"></div>
<div class="abs copy-block" style="left:137px;top:978px;width:492px">
  <div class="eyebrow">COMPANY BACKGROUND</div>
  <h2>DANGERS OF HEAD INJURY</h2>
  <p>More and more conversations are being had about concussion as a result of sporting injuries; a debate is ongoing about concussion in football and how dangerous is heading the ball, the impact of better understanding concussion in males and females is now the subject of medical journal articles, isolating the impact.</p>
  <a class="btn" href="#">READ MORE</a>
</div>
<div class="abs photo" style="left:676px;top:935px;width:451px;height:373px;background:linear-gradient(150deg,#5a6f9a,#b9c3cf 45%,#3d5ea8 70%,#8a2f3e)" role="img" aria-label="Photo of two players challenging for a header"></div>

<div class="abs mission">
  <h2>OUR MISSION</h2>
  <h3>HALOMARK – BRINGING SAFETY TO THE SPORTS CONCUSSION DEBATE</h3>
  <p>Halomark is designing and developing head protection products to reduce the likelihood of concussion when playing sports. Exploring and understanding medical insights, material science and composites research, current and former players experiences and governing bodies guidelines has allowed Halomark to develop the style, safety, form and function requirements of a suitable product to bring to market in Q4 2020.</p>
</div>

<!-- about product -->
<div class="abs photo" style="left:74px;top:1716px;width:451px;height:374px;background:radial-gradient(ellipse 45% 22% at 50% 50%,#4a4d55 0%,#6a6d73 60%,#ececec 100%)" role="img" aria-label="Product render of the protective headband"></div>
<div class="abs bracket" style="left:556px;top:1716px;width:423px;height:374px"></div>
<div class="abs copy-block" style="left:619px;top:1762px;width:500px">
  <div class="eyebrow">ABOUT</div>
  <h2>OUR PRODUCT</h2>
  <p>Halomark spans product strategy, market demand and positioning, product design requirements, product development and innovation, manufacturing, sales across markets and after-sales services. Our team bring together deep knowledge, unique connections and the experience of delivering high-profile and successful innovation.</p>
  <a class="btn" href="#">READ MORE</a>
</div>

<!-- features -->
<div class="abs rule"></div>
<h2 class="abs section-title" style="top:2208px">PRODUCT FEATURES</h2>

<div class="abs feature" style="left:64px;top:2294px"><div class="circle"><svg width="56" height="30" viewBox="0 0 56 30"><rect x="2" y="4" width="52" height="22" rx="10" fill="none" stroke="#fff" stroke-width="3"/><path d="M14 15h28" stroke="#fff" stroke-width="3"/></svg></div><div class="label">BRITISH DESIGNED</div></div>
<div class="abs feature" style="left:330px;top:2294px"><div class="circle"><svg width="44" height="50" viewBox="0 0 44 50"><path d="M22 3 L40 10 V24 C40 36 31 44 22 47 C13 44 4 36 4 24 V10Z" fill="none" stroke="#fff" stroke-width="3"/><path d="M14 24l6 6 11-12" stroke="#fff" stroke-width="3" fill="none"/></svg></div><div class="label">SAFETY TESTED</div></div>
<div class="abs feature" style="left:603px;top:2294px"><div class="circle"><svg width="50" height="44" viewBox="0 0 50 44"><path d="M6 38 C6 14 24 6 44 6 C44 28 32 38 12 38Z" fill="none" stroke="#fff" stroke-width="3"/><path d="M6 40 L30 18" stroke="#fff" stroke-width="3"/></svg></div><div class="label">ENVIRONMENTALLY FRIENDLY</div></div>
<div class="abs feature" style="left:869px;top:2294px"><div class="circle"><svg width="50" height="50" viewBox="0 0 50 50"><path d="M12 38 C12 20 26 8 44 6 C42 24 30 36 12 38Z" fill="none" stroke="#fff" stroke-width="3"/><path d="M8 44 L30 20 M4 46h42" stroke="#fff" stroke-width="3"/></svg></div><div class="label">LIGHT-WEIGHT</div></div>

<div class="abs feature" style="left:64px;top:2521px"><div class="circle"><svg width="46" height="46" viewBox="0 0 46 46"><rect x="4" y="20" width="9" height="20" fill="none" stroke="#fff" stroke-width="3"/><path d="M13 22 L22 6 C26 6 27 10 26 14 L25 18 H38 C41 18 42 21 41 24 L37 38 C36 40 34 40 32 40 H13" fill="none" stroke="#fff" stroke-width="3"/></svg></div><div class="label">COMFORTABLE</div></div>
<div class="abs feature" style="left:330px;top:2521px"><div class="circle"><svg width="50" height="46" viewBox="0 0 50 46"><path d="M8 40 C8 28 14 20 22 16 L30 10 M20 40 C22 30 30 24 40 22" fill="none" stroke="#fff" stroke-width="3"/><circle cx="38" cy="8" r="3" fill="#fff"/><circle cx="44" cy="14" r="2" fill="#fff"/><circle cx="12" cy="10" r="2" fill="#fff"/></svg></div><div class="label">WASHABLE, ANTIBACTERIAL FABRIC</div></div>
<div class="abs feature" style="left:603px;top:2521px"><div class="circle"><svg width="40" height="50" viewBox="0 0 40 50"><rect x="4" y="6" width="32" height="40" rx="2" fill="none" stroke="#fff" stroke-width="3"/><rect x="13" y="2" width="14" height="8" fill="#fff"/><path d="M10 20h20M10 28h20M10 36h20" stroke="#fff" stroke-width="3"/></svg></div><div class="label">RANGE OF SIZES</div></div>
<div class="abs feature" style="left:869px;top:2521px"><div class="circle"><svg width="50" height="46" viewBox="0 0 50 46"><rect x="18" y="4" width="24" height="20" fill="none" stroke="#fff" stroke-width="3"/><path d="M4 30 H16 L26 34 H38 V40 H4Z" fill="none" stroke="#fff" stroke-width="3"/></svg></div><div class="label">PRODUCT AVAILBILITY</div></div>

<a class="abs btn" href="#" style="left:526px;top:2722px;width:150px;text-align:center;padding:11px 0;margin-top:0">READ MORE</a>

<!-- team section background -->
<svg class="abs" style="top:2800px;left:0" width="1200" height="700" viewBox="0 0 1200 700">
  <path fill="#f3f3f3" d="M0 90 C150 80 300 110 450 100 C600 90 700 70 800 40 C900 10 1000 70 1200 60 L1200 660 C1000 700 700 640 500 670 C300 700 150 650 0 690Z"/>
</svg>
<h2 class="abs section-title team-title" style="top:3020px">OUR TEAM</h2>

<div class="abs member" style="left:89px;top:3101px"><div class="portrait" role="img" aria-label="Portrait of the founder"></div><h4>MARTIN ASHBY</h4><div class="role">FOUNDER / CEO</div><p>Martin has a wealth of experience of growing start-ups and exiting businesses, from professional services to technology companies.</p></div>
<div class="abs member" style="left:450px;top:3101px"><div class="portrait" role="img" aria-label="Portrait of the co-founder"></div><h4>HELEN CORRIGAN</h4><div class="role">CO -FOUNDER / COO</div><p>Helen has been planning and delivering commercial, large scale transformation projects within people based.</p></div>
<div class="abs member" style="left:811px;top:3101px"><div class="portrait" role="img" aria-label="Portrait of the commercial officer"></div><h4>DUNCAN ROWE</h4><div class="role">CCO</div><p>Duncan started his career in retail banking, later experience in corporate and private banking. Since leaving the corporate world in 2007.</p></div>

<!-- blog -->
<div class="abs bracket" style="left:74px;top:3507px;width:424px;height:374px;background:#fff;z-index:2"></div>
<div class="abs copy-block" style="left:137px;top:3566px;width:492px">
  <div class="eyebrow" style="font-size:30px;margin-bottom:14px">BLOG POSTS</div>
  <h4 style="font-size:16px;color:var(--blue);font-weight:700;margin-bottom:2px">LOREM IPSUM DOLOR SIT AMET...</h4>
  <p>Pellentesque condimentum lorem quis turpis facilisis, in venenatis nulla lobortis. Aenean ullamcorper ornare nisl vel venenatis. Cras nisi elit, hendrerit vitae ultrices eu, tincidunt in sem. Sed faucibus fringilla libero, vestibulum malesuada....</p>
  <a class="btn" href="#">READ MORE</a>
</div>
<div class="abs photo" style="left:676px;top:3507px;width:451px;height:374px;background:linear-gradient(170deg,#4a5060 0%,#7a7f88 30%,#c8372e 55%,#3f7a2e 75%,#2f5e24 100%)" role="img" aria-label="Photo of an injured player lying on the grass"></div>

<!-- distribution -->
<svg class="abs" style="top:3980px;left:0" width="1200" height="530" viewBox="0 0 1200 530">
  <path fill="#f3f3f3" d="M0 110 C200 130 350 60 550 70 C750 80 850 20 1000 10 C1100 5 1150 20 1200 30 L1200 530 L0 530Z"/>
</svg>
<div class="abs dist" style="top:4200px;left:0;width:1200px">
  <h2 class="section-title" style="position:static;color:#3a3a3a;font-weight:400;font-size:30px">DISTRIBUTION</h2>
  <p>From parents to clubs to federations our model is simple; parents of youth players, parents of amateur players, professional players and clubs, academies and all with the support of federations and unions.</p>
</div>
<div class="abs partners">
  <i style="width:150px;height:40px"></i>
  <i style="width:150px;height:56px;border-radius:28px"></i>
  <i style="width:44px;height:60px;border-radius:50%"></i>
  <i style="width:130px;height:54px"></i>
  <i style="width:44px;height:60px;border-radius:6px 6px 22px 22px"></i>
</div>

<!-- newsletter -->
<div class="abs newsletter">
  <div class="label">NEWSLETTER SIGN UP</div>
  <div class="field">Enter Email Address</div>
  <div class="go">GO</div>
  <div class="follow">FOLLOW US</div>
  <div class="socials"><i></i><i></i><i></i><i></i><i></i></div>
</div>

<!-- footer -->
<footer class="abs footer">
  <div class="f-brand">HALOMARK</div>
  <div class="copy">Copyright © 2020 Company Name<br>All rights reserved.</div>
  <div class="col" style="left:385px">
    <h5>SITE MAP</h5>
    <div class="split">
      <ul><li>Home</li><li>About Us</li><li>Services</li><li>Products</li></ul>
      <ul><li>Clients</li><li>News</li><li>Contact Us</li></ul>
    </div>
  </div>
  <div class="col" style="left:665px">
    <h5>RESOURCES</h5>
    <ul><li>Quisque a ultrices</li><li>Magna nec interdum</li><li>Nulla dignissim</li><li>Porttitor mauris</li></ul>
  </div>
  <div class="col" style="left:910px">
    <h5>QUICK LINKS</h5>
    <ul><li>Quisque a ultrices</li><li>Magna nec interdum</li><li>Nulla dignissim</li><li>Porttitor mauris</li></ul>
  </div>
</footer>

</body>
</html>
```